Visitenkarten für den Verkauf mediterraner Pflanzen
Zielgruppe
Verkauf winterharter mediterraner Pflanzen
Aufgabenstellung
Die Farben von der Homepage und eventuell die Schriftarten sollten übernommen werden um ein einheitliches Erscheinungsbild zu erzeugen

```html
<!DOCTYPE html>
<html lang="de">
<head>
<meta charset="utf-8">
<title>Solmara Gärten – Visitenkarten</title>
<link rel="stylesheet" href="https://fonts.googleapis.com/css2?family=Exo+2:wght@400;600;700&display=swap">
<style>
  :root {
    --bg: #eeeeef;
    --teal: #5e9e92;
    --teal-dark: #4d8a7f;
    --mint: #d6e6e3;
    --leaf: #4fb574;
    --ink: #26313b;
    --photo-dark: #5b6656;
    --photo-mid: #9aa392;
    --photo-light: #e2e4df;
  }
  * { box-sizing: border-box; margin: 0; padding: 0; }
  html, body { width: 1200px; height: 800px; overflow: hidden; }
  body {
    background: var(--bg);
    font-family: "Exo 2", sans-serif;
    position: relative;
  }
  .card {
    position: absolute;
    left: 330px;
    width: 540px;
    height: 330px;
    overflow: hidden;
    box-shadow: 0 6px 18px rgba(0,0,0,0.18);
  }
  .card--front { top: 45px; }
  .card--back { top: 420px; background: var(--mint); }

  /* Front */
  .front-photo {
    position: absolute; inset: 0 0 56px 0;
    background: linear-gradient(180deg, var(--photo-light) 0%, #c9cec4 35%, var(--photo-mid) 60%, var(--photo-dark) 100%);
  }
  .front-logo-panel {
    position: absolute;
    left: 70px; top: 70px;
    width: 400px; height: 130px;
    background: rgba(255,255,255,0.72);
    display: flex; align-items: center; gap: 20px;
    padding: 0 28px;
  }
  .front-band {
    position: absolute; left: 0; right: 0; bottom: 0;
    height: 56px; background: var(--teal);
    display: flex; align-items: center; justify-content: center;
    color: var(--mint); font-weight: 700; font-size: 17px; letter-spacing: 0.5px;
  }

  /* Brand lockup */
  .brand-dot { border-radius: 50%; background: var(--leaf); flex: none; }
  .brand-name { color: var(--ink); font-weight: 600; white-space: nowrap; }
  .front-logo-panel .brand-dot { width: 84px; height: 84px; }
  .front-logo-panel .brand-name { font-size: 30px; }

  /* Back */
  .back-photo {
    position: absolute; left: 0; top: 0; bottom: 0; width: 245px;
    background: linear-gradient(160deg, #e3e6e1 0%, #a9b2a2 40%, #6f7c63 70%, #d3d8cf 100%);
  }
  .back-name-box {
    position: absolute; left: 22px; bottom: 40px;
    width: 190px; padding: 12px 14px;
    background: rgba(255,255,255,0.82);
  }
  .person-name { font-size: 17px; font-weight: 700; color: var(--teal-dark); }
  .person-role { font-size: 15px; font-weight: 400; color: var(--ink); margin-top: 2px; }

  .back-info { position: absolute; left: 245px; right: 0; top: 0; bottom: 48px; padding: 26px 28px 0 44px; }
  .back-logo { display: flex; align-items: center; gap: 14px; margin-left: 18px; }
  .back-logo .brand-dot { width: 56px; height: 56px; }
  .back-logo .brand-name { font-size: 21px; }

  .company { margin-top: 34px; font-size: 15px; font-weight: 700; color: var(--teal); }
  .address { font-size: 14px; color: var(--teal-dark); margin-bottom: 10px; }
  .contact-list { list-style: none; }
  .contact-list li {
    display: flex; align-items: center; gap: 12px;
    font-size: 14px; color: var(--teal-dark); margin-bottom: 5px;
  }
  .contact-list svg { width: 15px; height: 15px; flex: none; }

  .back-band {
    position: absolute; left: 245px; right: 0; bottom: 0; height: 48px;
    background: var(--teal);
    display: flex; align-items: center; gap: 56px; padding-left: 24px;
  }
  .social { display: flex; align-items: center; gap: 10px; color: var(--mint); font-weight: 700; font-size: 15px; }
  .social-square { width: 18px; height: 18px; border: 2px solid var(--mint); border-radius: 3px; }
</style>
</head>
<body>

<section class="card card--front" aria-label="Vorderseite">
  <div class="front-photo" role="img" aria-label="Unscharfes Foto eines Palmblatts in Grün- und Grautönen"></div>
  <div class="front-logo-panel">
    <span class="brand-dot"></span>
    <span class="brand-name">Solmara Gärten</span>
  </div>
  <div class="front-band">www.solmara.at</div>
</section>

<section class="card card--back" aria-label="Rückseite">
  <div class="back-photo" role="img" aria-label="Foto: Gärtner schiebt eine Schubkarre durch ein Gewächshaus mit mediterranen Topfpflanzen"></div>
  <div class="back-name-box">
    <p class="person-name">Matthias Lehrbaum</p>
    <p class="person-role">Geschaftfuhrer</p>
  </div>

  <div class="back-info">
    <div class="back-logo">
      <span class="brand-dot"></span>
      <span class="brand-name">Solmara Gärten</span>
    </div>
    <p class="company">Solmara Gärten</p>
    <p class="address">Wiesenhof 14 8321 Sonnfeld</p>
    <ul class="contact-list">
      <li>
        <svg viewBox="0 0 16 16" aria-hidden="true"><rect x="1" y="3" width="14" height="10" fill="none" stroke="#5e9e92" stroke-width="1.5"/><path d="M1 3l7 6 7-6" fill="none" stroke="#5e9e92" stroke-width="1.5"/></svg>
        office@solmara.at
      </li>
      <li>
        <svg viewBox="0 0 16 16" aria-hidden="true"><path d="M4 1.5l2.5 3-1.5 1.8c.8 1.8 2.3 3.3 4.2 4.2l1.8-1.5 3 2.5-1.5 2.5C7 13.5 2.5 9 1.5 3z" fill="none" stroke="#5e9e92" stroke-width="1.4" stroke-linejoin="round"/></svg>
        +43 (0)660 5830142
      </li>
      <li>
        <svg viewBox="0 0 16 16" aria-hidden="true"><circle cx="8" cy="8" r="6.5" fill="none" stroke="#5e9e92" stroke-width="1.3"/><ellipse cx="8" cy="8" rx="3" ry="6.5" fill="none" stroke="#5e9e92" stroke-width="1.1"/><path d="M1.5 8h13M2.5 5h11M2.5 11h11" stroke="#5e9e92" stroke-width="1"/></svg>
        www.solmara.at
      </li>
    </ul>
  </div>

  <div class="back-band">
    <span class="social"><span class="social-square"></span>solmara</span>
    <span class="social"><span class="social-square"></span>solmara</span>
  </div>
</section>

</body>
</html>
```